Art Deco Wedding Invitation

We need a wedding invitation designed for a 1920's Art Deco theme.
The wedding will take place in Berlin, which had a glamorous, modern and wild culture in the 1920's. This may offer some design inspiration.
The couple's names are Rowland and Liora and the wedding will take place on May 8, 2015.

Industry/Entity Type

Wedding

```html
<!DOCTYPE html>
<html lang="en">
<head>
<meta charset="utf-8">
<title>Rowland &amp; Liora — Wedding Invitation</title>
<link rel="stylesheet" href="https://fonts.googleapis.com/css2?family=Pinyon+Script&family=Crimson+Pro:wght@400&display=swap">
<style>
  :root {
    --navy: #2f5886;
    --navy-deep: #2a5180;
    --navy-light: #35618f;
    --panel-top: #dfe6ef;
    --panel-bottom: #c9d5e3;
    --ivory: #ffffff;
    --ink-on-panel: #2a5180;
    --edge: rgba(255, 255, 255, 0.25);
    --shadow: rgba(10, 25, 50, 0.45);
  }
  * { margin: 0; padding: 0; box-sizing: border-box; }
  html, body {
    width: 1200px;
    height: 856px;
    overflow: hidden;
    background: var(--navy);
  }
  .invitation {
    position: relative;
    width: 1200px;
    height: 856px;
    background: radial-gradient(ellipse at 50% 45%, var(--navy-light) 0%, var(--navy) 60%, var(--navy-deep) 100%);
    box-shadow: inset 0 0 0 2px var(--edge);
    color: var(--ivory);
    font-family: "Crimson Pro", Georgia, serif;
    font-variant-numeric: lining-nums;
    text-align: center;
  }
  .line {
    position: absolute;
    left: 0;
    width: 100%;
    white-space: nowrap;
    font-weight: 400;
    line-height: 1;
  }
  .invitation__intro { top: 43px; font-size: 37px; }
  .name-panel {
    position: absolute;
    left: 196px;
    top: 113px;
    width: 807px;
    height: 377px;
    border-radius: 60px;
    background: linear-gradient(180deg, var(--panel-top), var(--panel-bottom));
    box-shadow: 1px 2px 3px var(--shadow);
  }
  .couple {
    top: 260px;
    font-family: "Pinyon Script", cursive;
    font-size: 80px;
    line-height: 1.2;
    color: var(--ink-on-panel);
  }
  .event__date { top: 530px; font-size: 37px; }
  .event__venue { top: 616px; font-size: 37px; }
  .event__address { top: 663px; font-size: 28px; }
  .event__rsvp { top: 734px; font-size: 30px; }
</style>
</head>
<body>
  <main class="invitation">
    <p class="line invitation__intro">Please join us to celebrate the marriage of</p>

    <div class="name-panel" role="img" aria-label="Ornamental white scrolled cartouche frame around the couple's names"></div>

    <h1 class="line couple">Rowland &amp; Liora</h1>

    <p class="line event__date">On Saturday, May 8th at Twelve O’clock</p>
    <p class="line event__venue">Halvern Museum &amp; Country Estate</p>
    <p class="line event__address">Route 18, Linden Pike - Berlin</p>
    <p class="line event__rsvp">Kindly respond by May 1st to Marta at (555) 010-2468</p>
  </main>
</body>
</html>
```